Trade Show Booth Sign Design for Retracting Banner

I need a trade show booth sign designed. It will be for a retractable banner that is double sided with 34 by 81 inch.

I want to incorporate my logo (see attached, have it in other file formats as well) and graphics from my website (https://www.dolbrookteachingadvisory.com/) with parts or all of the following text.

· Educational Content Creation
o Supplemental Textbook Content Development
o E-learning Content Development
· Curriculum Development
o KVTR/Bright Ladder
o Three Dimensional Learning
· Assessment
o Formative Assessments
o Elementary School, Middle School, High School, College, and Business
· Professional Development
o Training
o Facilitation

Target Market(s)

Education

Industry/Entity Type

Education

Font styles to use
Sans Serif

Colors

Designer to choose colors to be used in the design.

Requirements
Must have
• Eye catching and easy to read design
Nice to have
• Would like to see incorporation of my logo and some of the elements of my website images
Should not have
• N/A

```html
<!DOCTYPE html>
<html lang="en">
<head>
<meta charset="utf-8">
<title>Dolbrook Teaching Advisory – Booth Banner</title>
<link rel="stylesheet" href="https://fonts.googleapis.com/css2?family=Anton&family=Arimo:wght@400;700&family=Tinos&display=swap">
<style>
  :root {
    --navy: #1f2a5e;
    --blue: #3d85c6;
    --mist: #e5e6eb;
    --white: #ffffff;
    --ring: #c9cbd2;
  }
  * { margin: 0; padding: 0; box-sizing: border-box; }
  html, body { width: 1200px; height: 2848px; overflow: hidden; background: var(--white); }
  .banner { position: relative; width: 1200px; height: 2848px; background: var(--white); font-family: "Arimo", Arial, sans-serif; color: var(--navy); }

  .masthead { position: absolute; left: 0; top: 78px; width: 1200px; height: 336px; background: var(--navy); }
  .masthead__art { position: absolute; left: 22px; top: -44px; width: 426px; height: 426px; border-radius: 50%;
    background: radial-gradient(circle at 50% 45%, #ffffff 0%, #f2f3f6 70%, #e2e4ea 100%);
    border: 4px solid var(--ring); z-index: 2; }
  .brand { position: absolute; left: 488px; top: 52px; width: 670px; color: var(--white); }
  .brand__name { display: block; font-family: "Anton", Impact, sans-serif; font-size: 172px; line-height: 1; letter-spacing: 2px; }
  .brand__sub { display: block; font-family: "Tinos", "Times New Roman", serif; font-size: 68px; line-height: 1; margin-top: 14px; }

  .tagline { position: absolute; left: 0; top: 482px; width: 1110px; height: 142px; }
  .tagline svg { position: absolute; inset: 0; }
  .tagline__text { position: absolute; left: 96px; top: 22px; font-family: "Anton", Impact, sans-serif; font-size: 86px; line-height: 1; letter-spacing: 10px; color: var(--white); }

  .intro { position: absolute; left: 95px; top: 656px; width: 1000px; font-size: 33px; line-height: 46px; color: var(--navy); }
  .intro p + p { margin-top: 46px; }
  .intro strong { font-weight: 700; }

  .services { position: absolute; left: 0; top: 1035px; width: 1200px; height: 1650px; background: var(--mist); }

  .section-title { position: absolute; left: 72px; font-family: "Anton", Impact, sans-serif; font-weight: 400; font-size: 86px; line-height: 1; letter-spacing: 3px; color: var(--navy); }
  .rule { position: absolute; left: 72px; height: 8px; background: var(--blue); }

  .item { position: absolute; font-size: 37px; line-height: 54px; font-weight: 700; color: var(--navy); }
  .tick { position: absolute; width: 68px; height: 56px; }

  .feature-art { position: absolute; width: 334px; height: 334px; border-radius: 50%; background: var(--navy); border: 12px solid var(--ring); box-shadow: 0 0 0 3px #ffffff inset; }

  .footer { position: absolute; left: 0; top: 2685px; width: 1200px; height: 163px; background: var(--navy); display: flex; align-items: center; justify-content: center; }
  .footer__url { color: var(--white); font-weight: 700; font-size: 56px; letter-spacing: 0.5px; }
</style>
</head>
<body>
<svg width="0" height="0" style="position:absolute">
  <defs>
    <symbol id="tick" viewBox="0 0 68 56">
      <path d="M4 30 L22 48 L64 6" fill="none" stroke="#3d85c6" stroke-width="11" stroke-linecap="round" stroke-linejoin="round"/>
    </symbol>
  </defs>
</svg>

<main class="banner">
  <header class="masthead">
    <div class="masthead__art" role="img" aria-label="Illustration of a head in profile with a glowing light bulb, gears, clouds and question marks"></div>
    <div class="brand">
      <span class="brand__name">DOLBROOK</span>
      <span class="brand__sub">Teaching Advisory</span>
    </div>
  </header>

  <div class="tagline">
    <svg width="1110" height="142" viewBox="0 0 1110 142"><polygon points="0,0 1110,0 1030,142 0,142" fill="#3d85c6"/></svg>
    <div class="tagline__text">LEARN. GROW. KNOW.</div>
  </div>

  <section class="intro">
    <p><strong>Dolbrook Teaching Advisory</strong> delivers research-based educational products for both the K-16 and corporate settings.</p>
    <p><strong>Dolbrook Teaching Advisory</strong> utilizes learning theory and content expertise to develop content that will stick with people (students or employees) and/or truly assess what they understand.</p>
  </section>

  <section class="services">
    <div class="feature-art" style="left:810px; top:-27px;" role="img" aria-label="Illustration of a presenter beside a projected chart speaking to a seated audience"></div>
    <div class="feature-art" style="left:812px; top:830px;" role="img" aria-label="Illustration of a flask surrounded by science and learning icons"></div>

    <h2 class="section-title" style="top:72px;">EDUCATIONAL<br>CONTENT CREATION</h2>
    <div class="rule" style="top:253px; width:773px;"></div>
    <svg class="tick" style="left:76px; top:301px;"><use href="#tick"/></svg>
    <div class="item" style="left:182px; top:300px;">Supplemental Textbook Content<br>Development</div>
    <svg class="tick" style="left:76px; top:454px;"><use href="#tick"/></svg>
    <div class="item" style="left:182px; top:457px;">E-learning Content Development</div>

    <h2 class="section-title" style="top:585px;">CURRICULUM DEVELOPMENT</h2>
    <div class="rule" style="top:680px; width:992px;"></div>
    <svg class="tick" style="left:76px; top:730px;"><use href="#tick"/></svg>
    <div class="item" style="left:182px; top:724px;">KVTR/Bright Ladder</div>
    <svg class="tick" style="left:76px; top:838px;"><use href="#tick"/></svg>
    <div class="item" style="left:182px; top:832px;">Three Dimensional Learning</div>

    <h2 class="section-title" style="top:952px;">ASSESSMENT</h2>
    <div class="rule" style="top:1043px; width:745px;"></div>
    <svg class="tick" style="left:76px; top:1096px;"><use href="#tick"/></svg>
    <div class="item" style="left:182px; top:1090px;">Formative Assessments</div>
    <svg class="tick" style="left:76px; top:1204px;"><use href="#tick"/></svg>
    <div class="item" style="left:182px; top:1200px;">Elementary School, Middle School,<br>High School, College, and Business</div>

    <h2 class="section-title" style="top:1396px;">PROFESSIONAL DEVELOPMENT</h2>
    <div class="rule" style="top:1490px; width:1024px;"></div>
    <svg class="tick" style="left:76px; top:1540px;"><use href="#tick"/></svg>
    <div class="item" style="left:182px; top:1534px;">Training</div>
    <svg class="tick" style="left:642px; top:1540px;"><use href="#tick"/></svg>
    <div class="item" style="left:741px; top:1534px;">Facilitation</div>
  </section>

  <footer class="footer">
    <span class="footer__url">www.DolbrookTeachingAdvisory.com</span>
  </footer>
</main>
</body>
</html>
```